Family Owned and Operated Spray Foam Insulation Company needs a business card design

We're a new company based in the heart of Texas (Fort Worth). We spray foam insulation into residential houses, commercial buildings, metal buildings, etc. Spray foam insulation provides a huge reduction in energy/costs so that is what drives our market. We like the primary colors but are open to suggestions and are coming to the experts for some creativity. I'm attaching a picture of shirt mock up we have with KLB on the front to show what we were leaning towards as well as some business cards that I find striking and memorable. I'm looking for a card that is clean and professional with a bit of edge. Note: My computer won't pull up the color samples below for me to choose so it's in your hands.

Target Market(s)

Professional custom home builders, construction industry, home owners

Industry/Entity Type

Residential

Contact Information for Business Card

Name: Marcus Kettle (no title) Phone #: 817-555-0148, address: 4087 larkmoor ave fort worth tx 76110, email: marcus@klbinsulation-example.com, website: klbinsulation-example.com

Requirements
Must have
• We want the words KLB and Kettle Spray Foam Insulation showcased on the card but hopefully on opposite sides
Should not have
• Any type of spray foam gun or splatter clip art

```html
<!DOCTYPE html>
<html lang="en">
<head>
<meta charset="utf-8">
<title>Kettle Spray Foam Insulation – Business Card</title>
<link rel="stylesheet" href="https://fonts.googleapis.com/css2?family=Arvo:wght@700&family=Cinzel:wght@600&family=Montserrat:wght@500&family=Roboto+Condensed:wght@300&display=swap">
<style>
  :root {
    --navy: #0a1f87;
    --front-outer: #9b9b9b;
    --front-inner: #aaaaaa;
    --back-fill: #d6d6d6;
    --mark-faint: #c0c5e0;
    --page: #ffffff;
  }
  html, body {
    margin: 0;
    width: 1007px;
    height: 1200px;
    overflow: hidden;
    background: var(--page);
  }
  .card {
    position: absolute;
    left: 4px;
    width: 991px;
    height: 538px;
    box-sizing: border-box;
    border: 5px solid var(--navy);
    overflow: hidden;
  }
  /* Front */
  .card--front {
    top: 4px;
    background: var(--front-outer);
  }
  .front__frame {
    position: absolute;
    left: 21px; top: 17px; right: 21px; bottom: 17px;
    border: 11px solid var(--navy);
    background: var(--front-inner);
    display: flex;
    flex-direction: column;
    align-items: center;
    justify-content: center;
  }
  .brand-name {
    font-family: "Arvo", Georgia, serif;
    font-weight: 700;
    color: var(--navy);
    line-height: 1;
    margin: 0;
  }
  .front__brand {
    font-size: 190px;
    margin-top: 20px;
  }
  .brand-tagline {
    font-family: "Cinzel", "Times New Roman", serif;
    font-weight: 600;
    color: var(--navy);
    margin: 0;
    white-space: nowrap;
  }
  .front__tagline {
    font-size: 27px;
    letter-spacing: 1px;
    margin-top: 6px;
  }
  /* Back */
  .card--back {
    top: 605px;
    height: 540px;
    border-width: 7px;
    background: var(--back-fill);
  }
  .back__mark {
    position: absolute;
    left: 20px;
    bottom: -60px;
    font-size: 470px;
    color: var(--mark-faint);
    line-height: 1;
    margin: 0;
    user-select: none;
  }
  .back__name {
    position: absolute;
    left: 70px;
    top: 52px;
    margin: 0;
    font-family: "Arvo", Georgia, serif;
    font-weight: 700;
    font-size: 52px;
    color: var(--navy);
    letter-spacing: 0.5px;
  }
  .contact-list {
    position: absolute;
    left: 118px;
    top: 134px;
    margin: 0;
    padding: 0;
    list-style: none;
    font-family: "Montserrat", Arial, sans-serif;
    font-weight: 500;
    color: var(--navy);
  }
  .contact-list li {
    display: flex;
    align-items: center;
    gap: 6px;
    height: 42px;
    font-size: 21px;
    letter-spacing: 0.5px;
  }
  .contact-list li.contact--address { font-size: 17px; }
  .contact-list svg { flex: none; }
  .back__signoff {
    position: absolute;
    right: 12px;
    bottom: 12px;
    text-align: center;
  }
  .back__brand { font-size: 58px; }
  .back__tagline {
    font-size: 10px;
    margin-top: 2px;
  }
  .back__website {
    margin: 6px 0 0;
    font-family: "Roboto Condensed", "Arial Narrow", sans-serif;
    font-weight: 300;
    font-size: 32px;
    color: var(--navy);
    text-align: right;
  }
</style>
</head>
<body>

<section class="card card--front" aria-label="Card front">
  <div class="front__frame">
    <p class="brand-name front__brand">KLB</p>
    <p class="brand-tagline front__tagline">Kettle Spray Foam Insulation</p>
  </div>
</section>

<section class="card card--back" aria-label="Card back">
  <p class="brand-name back__mark" aria-hidden="true">KLB</p>

  <h1 class="back__name">MARCUS KETTLE</h1>

  <ul class="contact-list">
    <li class="contact--email">
      <svg width="38" height="30" viewBox="0 0 38 30" aria-hidden="true">
        <rect x="1.5" y="1.5" width="35" height="27" rx="13.5" fill="none" stroke="#0a1f87" stroke-width="2.5"/>
        <rect x="10" y="9" width="18" height="12" fill="none" stroke="#0a1f87" stroke-width="2"/>
        <path d="M10 9 L19 16 L28 9" fill="none" stroke="#0a1f87" stroke-width="2"/>
      </svg>
      marcus@klbinsulation-example.com
    </li>
    <li class="contact--phone">
      <svg width="38" height="30" viewBox="0 0 38 30" aria-hidden="true">
        <rect x="1.5" y="1.5" width="35" height="27" rx="13.5" fill="none" stroke="#0a1f87" stroke-width="2.5"/>
        <path d="M12 8 C11 12 15 20 22 23 L25 20 L21 17 L19 19 C17 18 15 15 14 13 L16 11 L14 7 Z" fill="#0a1f87"/>
      </svg>
      817-555-0148
    </li>
    <li class="contact--address">
      <svg width="26" height="30" viewBox="0 0 26 30" aria-hidden="true">
        <path d="M13 2 C7 2 3 6 3 11 C3 18 13 28 13 28 C13 28 23 18 23 11 C23 6 19 2 13 2 Z" fill="none" stroke="#0a1f87" stroke-width="2.8"/>
        <circle cx="13" cy="11" r="3.5" fill="#0a1f87"/>
      </svg>
      4087 Larkmoor Ave Fort Worth tx 76110
    </li>
  </ul>

  <div class="back__signoff">
    <p class="brand-name back__brand">KLB</p>
    <p class="brand-tagline back__tagline">Kettle Spray Foam Insulation</p>
    <p class="back__website">klbinsulation-example.com</p>
  </div>
</section>

</body>
</html>
```